17 Ways Your Nest Egg Can Bloom Book Cover

I need a book cover for a softcover book I will market directly.
The name of the book will be.
"17 Ways Your Nest Egg Can Bloom!"

I'm open to any and all ideas. But I want the book cover to stand out, to draw people's interest. But feel free to use your skill set to come up with good ideas.

I will be selling this book door to door and onine as well.

Target Market(s)

45-60 year old married couples

Industry/Entity Type

Financial Planning

Colors

Designer to choose colors to be used in the design.

Requirements
Must have
• website address.
• www.lanternoakadvisors.com
Nice to have
• like to have my picture on the back cover, with my company logo too if possible.

```html
<!DOCTYPE html>
<html lang="en">
<head>
<meta charset="UTF-8">
<title>17 Ways Your Nest Egg Can Bloom – Book Cover</title>
<link rel="stylesheet" href="https://fonts.googleapis.com/css2?family=Playfair+Display:wght@700;900&family=Libre+Baskerville:ital,wght@0,400;0,700;1,400&family=Oswald:wght@400;500&family=Cormorant+Garamond:wght@500&display=swap">
<style>
  :root {
    --stage: #e9eaec;
    --cover-deep: #2a3592;
    --cover-mid: #27409f;
    --cover-glow: #1d7cc8;
    --gold-light: #f3d77a;
    --gold: #d2a93c;
    --gold-dark: #a9801f;
    --white: #ffffff;
    --author-blue: #1b6fc4;
    --hand-grey: #9a9ca3;
    --jar-grey: #c9ced6;
  }
  * { box-sizing: border-box; margin: 0; padding: 0; }
  html, body {
    width: 1200px;
    height: 800px;
    overflow: hidden;
    background: var(--stage);
  }
  .stage {
    width: 1200px;
    height: 800px;
    display: flex;
    align-items: center;
    justify-content: center;
  }
  .cover {
    position: relative;
    width: 500px;
    height: 750px;
    overflow: hidden;
    background:
      radial-gradient(ellipse 70% 45% at 70% 78%, var(--cover-glow) 0%, rgba(29,124,200,0) 100%),
      linear-gradient(180deg, var(--cover-deep) 0%, var(--cover-mid) 100%);
    box-shadow: 0 18px 40px rgba(0,0,0,0.18);
  }
  .title-frame {
    position: absolute;
    left: 30px;
    top: 32px;
    width: 440px;
    height: 392px;
    border: 2px solid var(--white);
  }
  .title-number {
    position: absolute;
    left: 0;
    right: 0;
    top: 58px;
    text-align: center;
    font-family: "Playfair Display", serif;
    font-weight: 900;
    font-size: 160px;
    line-height: 1;
    color: var(--gold);
    background: linear-gradient(180deg, var(--gold-light) 0%, var(--gold) 55%, var(--gold-dark) 100%);
    -webkit-background-clip: text;
    background-clip: text;
    -webkit-text-fill-color: transparent;
  }
  .title-words {
    position: absolute;
    left: 0;
    right: 0;
    top: 226px;
    text-align: center;
    font-family: "Libre Baskerville", serif;
    color: var(--white);
    line-height: 1.04;
  }
  .title-words .line { display: block; font-size: 46px; }
  .title-words .line-small { font-size: 44px; }
  .title-words em { font-style: italic; }
  .author-bar {
    position: absolute;
    left: 236px;
    top: 404px;
    width: 246px;
    height: 40px;
    background: var(--white);
    display: flex;
    align-items: center;
    justify-content: center;
    font-family: "Oswald", sans-serif;
    font-weight: 500;
    font-size: 24px;
    letter-spacing: 4px;
    color: var(--author-blue);
  }
  .author-rule {
    position: absolute;
    left: 120px;
    top: 438px;
    width: 362px;
    height: 6px;
    background: var(--author-blue);
    border-top: 2px solid var(--white);
  }
  .art-hand {
    position: absolute;
    left: 0;
    top: 446px;
    width: 230px;
    height: 64px;
  }
  .art-jar {
    position: absolute;
    left: 300px;
    top: 500px;
    width: 110px;
    height: 150px;
  }
  .website {
    position: absolute;
    right: 28px;
    bottom: 26px;
    font-family: "Cormorant Garamond", serif;
    font-weight: 500;
    font-size: 15px;
    letter-spacing: 0.5px;
    color: var(--white);
  }
</style>
</head>
<body>
<main class="stage">
  <section class="cover" aria-label="Front cover">
    <div class="title-frame"></div>
    <h1 class="book-title">
      <span class="title-number">17</span>
      <span class="title-words">
        <span class="line">Ways</span>
        <span class="line line-small">Your Nest Egg</span>
        <span class="line"><em>Can</em> Bloom!</span>
      </span>
    </h1>
    <div class="author-rule"></div>
    <div class="author-bar">AUTHOR MILES</div>

    <svg class="art-hand" role="img" aria-label="Photo of a hand holding out a banknote toward the savings jar" viewBox="0 0 230 64" preserveAspectRatio="none">
      <defs>
        <linearGradient id="handTone" x1="0" y1="0" x2="1" y2="0">
          <stop offset="0" stop-color="#b9bbc1"/>
          <stop offset="1" stop-color="#8e9096"/>
        </linearGradient>
      </defs>
      <rect x="0" y="0" width="230" height="64" rx="8" fill="url(#handTone)"/>
    </svg>

    <svg class="art-jar" role="img" aria-label="Photo of a glass savings jar filled with coins and bills" viewBox="0 0 110 150" preserveAspectRatio="none">
      <defs>
        <linearGradient id="jarTone" x1="0" y1="0" x2="0" y2="1">
          <stop offset="0" stop-color="#e3e6ea"/>
          <stop offset="1" stop-color="#9ea6b2"/>
        </linearGradient>
      </defs>
      <rect x="0" y="0" width="110" height="150" rx="22" fill="url(#jarTone)"/>
    </svg>

    <p class="website">www.lanternoakadvisors.com</p>
  </section>
</main>
</body>
</html>
```